Pediatric Dentist Business Card

I need a business card designed for a dentist who works exclusively with children.
We prefer designs that are out of ordiary that is fun and interesting to kids.

there is no logo since this is a dentists office. The name of the doctor is "Tavor Kesh" if you want to get creative with that.

Target Market(s)

Kids

Industry/Entity Type

Business

Contact Information for Business Card

Anythings that is creative

Colors

Designer to choose colors to be used in the design.

```html
<!DOCTYPE html>
<html lang="en">
<head>
<meta charset="utf-8">
<title>Pediatric Dentist Business Card</title>
<link href="https://fonts.googleapis.com/css2?family=Quicksand:wght@500;600&family=Open+Sans:wght@600&display=swap" rel="stylesheet">
<style>
  :root {
    --sky: #22c1f3;
    --white: #ffffff;
    --ink: #1b1b1b;
    --page: #eef1f3;
    --photo-light: #d9d9dc;
    --photo-mid: #c99a82;
    --photo-warm: #e2476b;
  }
  html, body {
    margin: 0;
    padding: 0;
    width: 1200px;
    height: 1135px;
    overflow: hidden;
    background: var(--page);
  }
  .canvas {
    position: relative;
    width: 1200px;
    height: 1135px;
  }
  .card {
    position: absolute;
    left: 235px;
    width: 680px;
    height: 406px;
    overflow: hidden;
    box-shadow: 0 10px 24px rgba(0,0,0,0.18);
  }
  .card--front { top: 90px; background: var(--sky); }
  .card--back { top: 625px; background: var(--white); }

  .card__art {
    position: absolute;
    inset: 0;
    width: 680px;
    height: 406px;
  }
  .contact-list {
    position: absolute;
    left: 125px;
    top: 130px;
    margin: 0;
    padding: 0;
    list-style: none;
  }
  .contact-list__item {
    display: flex;
    align-items: center;
    height: 21px;
    margin-bottom: 21px;
    font-family: "Open Sans", sans-serif;
    font-weight: 600;
    font-size: 13.5px;
    color: var(--white);
  }
  .contact-list__icon {
    width: 20px;
    height: 20px;
    margin-right: 13px;
    flex: none;
  }
  .identity {
    position: absolute;
    left: 421px;
    top: 174px;
    width: 200px;
    text-align: center;
    color: var(--white);
    font-family: "Quicksand", sans-serif;
  }
  .identity__name {
    margin: 0;
    font-size: 28px;
    font-weight: 600;
    line-height: 1.1;
  }
  .identity__title {
    margin: 2px 0 0;
    font-size: 14px;
    font-weight: 600;
  }
</style>
</head>
<body>
<main class="canvas">

  <section class="card card--front" aria-label="Card front">
    <svg class="card__art" viewBox="0 0 680 406" aria-hidden="true">
      <circle cx="190" cy="210" r="165" fill="var(--white)"/>
      <circle cx="164" cy="208" r="163" fill="var(--sky)"/>
    </svg>

    <ul class="contact-list">
      <li class="contact-list__item">
        <svg class="contact-list__icon" viewBox="0 0 20 20" aria-hidden="true">
          <rect x="1" y="1" width="18" height="18" rx="4" fill="var(--white)" stroke="var(--ink)" stroke-width="2"/>
          <path d="M7 5 l2 3 -1.2 1.2 a6 6 0 0 0 3 3 L12 11 l3 2 -1 2 C9 15 5 11 5 6 Z" fill="var(--sky)"/>
        </svg>
        123456789
      </li>
      <li class="contact-list__item">
        <svg class="contact-list__icon" viewBox="0 0 20 20" aria-hidden="true">
          <rect x="1" y="1" width="18" height="18" rx="4" fill="var(--white)" stroke="var(--ink)" stroke-width="2"/>
          <rect x="5" y="6.5" width="10" height="7" rx="1" fill="var(--sky)"/>
        </svg>
        aaa@gamil.com
      </li>
      <li class="contact-list__item">
        <svg class="contact-list__icon" viewBox="0 0 20 20" aria-hidden="true">
          <rect x="1" y="1" width="18" height="18" rx="4" fill="var(--white)" stroke="var(--ink)" stroke-width="2"/>
          <circle cx="10" cy="10" r="5" fill="var(--sky)"/>
          <path d="M5 10 h10 M10 5 v10" stroke="var(--white)" stroke-width="0.8"/>
        </svg>
        www.aaaaa.com
      </li>
      <li class="contact-list__item">
        <svg class="contact-list__icon" viewBox="0 0 20 20" aria-hidden="true">
          <rect x="1" y="1" width="18" height="18" rx="4" fill="var(--white)" stroke="var(--ink)" stroke-width="2"/>
          <path d="M10 16 C7 12 6 10.5 6 8.5 a4 4 0 0 1 8 0 c0 2 -1 3.5 -4 7.5 Z" fill="var(--sky)"/>
          <circle cx="10" cy="8.5" r="1.5" fill="var(--white)"/>
        </svg>
        aaaaaaaaaaaaaaa
      </li>
    </ul>

    <div class="identity">
      <h1 class="identity__name">Your Name</h1>
      <p class="identity__title">Title</p>
    </div>
  </section>

  <section class="card card--back" aria-label="Card back">
    <svg class="card__art" viewBox="0 0 680 406">
      <defs>
        <linearGradient id="photo-tones" x1="0" y1="0" x2="1" y2="1">
          <stop offset="0" stop-color="var(--photo-light)"/>
          <stop offset="0.5" stop-color="var(--photo-mid)"/>
          <stop offset="1" stop-color="var(--photo-warm)"/>
        </linearGradient>
      </defs>
      <rect class="tooth-area" role="img" aria-label="Blue tooth illustration"
        x="88" y="110" width="140" height="184" rx="10" fill="var(--sky)"/>
      <polygon class="accent-band" aria-hidden="true" fill="var(--sky)"
        points="512,0 680,0 680,406 375,406 237,175"/>
      <polygon class="photo-area" role="img" aria-label="Photo of a smiling child brushing her teeth"
        fill="url(#photo-tones)"
        points="538,0 680,0 680,406 394,406 256,175"/>
    </svg>
  </section>

</main>
</body>
</html>
```